Lantern Hour 2017 (an advertisement for a musical Christian presentation)

This postcard will advertise a Christian MUSICAL show celebrating the 2017 New Year. Graphics needs to indicate musical content, Colors are December advertising.

We will need all of the layers unlocked in PSD format
Our logo is attached

TITLE: Lantern Hour 2017
SUBTITLE: You're Invited
TIME: December 31, 2016 at 11:00PM

Target Market(s)

Christians that have been attendees to our church

Industry/Entity Type

Non-Profit

Font styles to use
Sans Serif
Script

Requirements
Must have
• Must have a modern look and feel and caught the eye in the mailbox.
• Musical content indicated in background
Nice to have
• December marketing colors
• Strong Fontology
Should not have
• Should not have styles not relevant in the US

```html
<!DOCTYPE html>
<html lang="en">
<head>
<meta charset="utf-8">
<title>Lantern Hour 2017 – Postcard</title>
<link rel="stylesheet" href="https://fonts.googleapis.com/css2?family=Marcellus&family=Open+Sans:wght@300&family=Yellowtail&display=swap">
<style>
  :root {
    --page: #e6e6e6;
    --paper-light: #ebe7e2;
    --paper-mid: #c9c4bf;
    --paper-dark: #a9a39e;
    --red: #d42a33;
    --red-deep: #9e1a20;
    --stripe: #d6d6d8;
    --stripe-shade: #b9b9bd;
    --white: #ffffff;
  }
  * { margin: 0; padding: 0; box-sizing: border-box; }
  html, body {
    width: 1200px;
    height: 960px;
    overflow: hidden;
    background: var(--page);
  }
  .postcard {
    position: absolute;
    left: 60px;
    top: 120px;
    width: 1080px;
    height: 720px;
    overflow: hidden;
    box-shadow: 0 10px 30px rgba(0,0,0,0.18);
  }
  .postcard__photo {
    position: absolute;
    inset: 0;
    background:
      radial-gradient(circle at 62% 30%, rgba(214,170,90,0.55) 0 9%, transparent 10%),
      radial-gradient(circle at 84% 33%, rgba(170,28,36,0.75) 0 10%, transparent 11%),
      radial-gradient(circle at 78% 55%, rgba(150,22,30,0.7) 0 7%, transparent 8%),
      linear-gradient(160deg, var(--paper-dark) 0%, var(--paper-mid) 40%, var(--paper-light) 100%);
  }
  .postcard__band {
    position: absolute;
    inset: 0;
    width: 1080px;
    height: 720px;
  }
  .postcard__heading {
    position: absolute;
    left: 32px;
    top: 30px;
    color: var(--white);
  }
  .postcard__title {
    font-family: "Marcellus", serif;
    font-weight: 400;
    font-size: 44px;
    letter-spacing: 2px;
    text-transform: uppercase;
    line-height: 1;
  }
  .postcard__year {
    font-family: "Open Sans", sans-serif;
    font-weight: 300;
    font-size: 200px;
    letter-spacing: -8px;
    line-height: 0.9;
    margin-top: 10px;
    margin-left: -6px;
  }
  .postcard__time {
    font-family: "Marcellus", serif;
    font-size: 40px;
    text-transform: uppercase;
    margin-top: 28px;
    line-height: 1;
  }
  .postcard__invite {
    position: absolute;
    left: 60px;
    top: 585px;
    font-family: "Yellowtail", cursive;
    font-size: 60px;
    color: var(--white);
    line-height: 1;
  }
  .postcard__brand {
    position: absolute;
    right: 48px;
    top: 578px;
    font-family: "Marcellus", serif;
    font-size: 56px;
    color: var(--white);
    line-height: 1;
  }
</style>
</head>
<body>
  <article class="postcard">
    <div class="postcard__photo" role="img" aria-label="Photograph of sheet music with gold and red Christmas ornaments and curled ribbon"></div>

    <svg class="postcard__band" viewBox="0 0 1080 720" aria-hidden="true">
      <defs>
        <linearGradient id="bandRed" x1="0" y1="0" x2="1" y2="0">
          <stop offset="0" stop-color="var(--red)"/>
          <stop offset="1" stop-color="var(--red-deep)"/>
        </linearGradient>
        <linearGradient id="bandStripe" x1="0" y1="0" x2="1" y2="0">
          <stop offset="0" stop-color="var(--stripe-shade)"/>
          <stop offset="1" stop-color="var(--stripe)"/>
        </linearGradient>
      </defs>
      <path d="M0 470 Q 420 555 1080 385 L1080 720 L0 720 Z" fill="url(#bandStripe)"/>
      <path d="M0 495 Q 420 578 1080 410 L1080 720 L0 720 Z" fill="var(--white)"/>
      <path d="M0 508 Q 420 590 1080 422 L1080 720 L0 720 Z" fill="url(#bandRed)"/>
    </svg>

    <header class="postcard__heading">
      <h1 class="postcard__title">Lantern Hour</h1>
      <p class="postcard__year">2017</p>
      <p class="postcard__time">31, 2016 at 11:00PM</p>
    </header>

    <p class="postcard__invite">You're Invited</p>
    <p class="postcard__brand">Crestview</p>
  </article>
</body>
</html>
```